Redesign of Wine Label

A redesign of a French wine label (attached below - Images 1-3) that changes the following elements:
- Change out the ducks on a bicycle for a man on an old-fashioned bicycle (such as a penny-farthing bicycle) wearing the traditional hat of Gascogne, France (please see the following link - https://www.picsharely.com/domaine_morvenol/ - where you can find many examples of the red hat referenced)
- Please rearrange the words "Domaine Morvenol" so that the word "Morvenol" is larger, about double the size of the word "Domaine"
- Please include the words "Les Cousins" somewhere around "Domaine Morvenol" in a manner that shows the connection.
- Please include the words "Côtes de Gascogne" somewhere in smaller, though clearly visible, letters closer to the bottom of the label.
- Please make the bicycle like the old image attached, with two aristocratic men in the same type of clothing riding it.

```html
<!DOCTYPE html>
<html lang="fr">
<head>
<meta charset="utf-8">
<title>Domaine Morvenol – Malbec label</title>
<link rel="stylesheet" href="https://fonts.googleapis.com/css2?family=Cormorant+Garamond:wght@400;500&family=Libre+Caslon+Text:wght@400&family=Montserrat:wght@300&family=Pinyon+Script&display=swap">
<style>
  :root {
    --backdrop: #ecebe7;
    --label-paper: #fdfdfc;
    --ink: #2b2b2b;
    --ink-soft: #3a3a3a;
    --ink-muted: #6f6f6f;
    --beret-red: #c7261f;
    --wheel-cream: #eee6d2;
    --shirt-navy: #33405a;
  }
  * { margin: 0; padding: 0; box-sizing: border-box; }
  html, body {
    width: 1125px;
    height: 1200px;
    overflow: hidden;
    background: var(--backdrop);
  }
  .label-sheet {
    width: 1125px;
    height: 1200px;
    display: flex;
    justify-content: center;
    align-items: center;
    gap: 45px;
  }
  .wine-label {
    position: relative;
    width: 500px;
    height: 550px;
    background: var(--label-paper);
    box-shadow: 0 2px 10px rgba(0,0,0,0.08);
    color: var(--ink);
    text-align: center;
  }
  .estate-prefix {
    position: absolute;
    top: 26px;
    left: 0;
    width: 100%;
    font-family: "Cormorant Garamond", serif;
    font-weight: 400;
    font-size: 34px;
    letter-spacing: 6px;
    color: var(--ink-soft);
  }
  .estate-name {
    position: absolute;
    top: 60px;
    left: 0;
    width: 100%;
    font-family: "Libre Caslon Text", serif;
    font-weight: 400;
    font-size: 76px;
    letter-spacing: 1px;
    line-height: 1;
    color: var(--ink);
  }
  .rider-illustration {
    position: absolute;
    top: 140px;
    left: 130px;
    width: 240px;
    height: 290px;
  }
  .house-signature {
    position: absolute;
    top: 200px;
    left: 318px;
    font-family: "Pinyon Script", cursive;
    font-size: 19px;
    color: var(--ink-soft);
  }
  .grape-variety {
    position: absolute;
    top: 440px;
    left: 0;
    width: 100%;
    font-family: "Cormorant Garamond", serif;
    font-weight: 500;
    font-size: 31px;
    letter-spacing: 5px;
    color: var(--ink-soft);
  }
  .appellation {
    position: absolute;
    top: 480px;
    left: 0;
    width: 100%;
    font-family: "Libre Caslon Text", serif;
    font-size: 23px;
    color: var(--ink);
  }
  .bottling-note {
    position: absolute;
    top: 514px;
    left: 0;
    width: 100%;
    font-family: "Montserrat", sans-serif;
    font-weight: 300;
    font-size: 15px;
    letter-spacing: 1px;
    color: var(--ink-muted);
  }
</style>
</head>
<body>
<main class="label-sheet">

  <section class="wine-label wine-label--colour">
    <div class="estate-prefix">DOMAINE</div>
    <div class="estate-name">MORVENOL</div>
    <svg class="rider-illustration" viewBox="0 0 240 290" role="img" aria-label="Illustration of a man in a red Gascon beret and striped shirt riding a penny-farthing bicycle">
      <defs>
        <linearGradient id="rider-tones-colour" x1="0" y1="0" x2="0" y2="1">
          <stop offset="0" stop-color="var(--beret-red)" stop-opacity="0.55"/>
          <stop offset="0.18" stop-color="var(--shirt-navy)" stop-opacity="0.35"/>
          <stop offset="0.5" stop-color="var(--wheel-cream)"/>
          <stop offset="1" stop-color="var(--wheel-cream)" stop-opacity="0.6"/>
        </linearGradient>
      </defs>
      <rect width="240" height="290" rx="6" fill="url(#rider-tones-colour)"/>
    </svg>
    <div class="house-signature">Les Cousins</div>
    <div class="grape-variety">MALBEC</div>
    <div class="appellation">CÔTES DE GASCOGNE</div>
    <div class="bottling-note">MIS EN BOUTEILLE À LA PROPRIÉTÉ</div>
  </section>

  <section class="wine-label wine-label--ink">
    <div class="estate-prefix">DOMAINE</div>
    <div class="estate-name">MORVENOL</div>
    <svg class="rider-illustration" viewBox="0 0 240 290" role="img" aria-label="Ink illustration of a man in a red Gascon beret riding a penny-farthing bicycle">
      <defs>
        <linearGradient id="rider-tones-ink" x1="0" y1="0" x2="0" y2="1">
          <stop offset="0" stop-color="var(--beret-red)" stop-opacity="0.45"/>
          <stop offset="0.2" stop-color="var(--ink)" stop-opacity="0.3"/>
          <stop offset="0.55" stop-color="#e4e4e2"/>
          <stop offset="1" stop-color="#efefed"/>
        </linearGradient>
      </defs>
      <rect width="240" height="290" rx="6" fill="url(#rider-tones-ink)"/>
    </svg>
    <div class="house-signature">Les Cousins</div>
    <div class="grape-variety">MALBEC</div>
    <div class="appellation">CÔTES DE GASCOGNE</div>
    <div class="bottling-note">MIS EN BOUTEILLE À LA PROPRIÉTÉ</div>
  </section>

</main>
</body>
</html>
```